SunnyPawGlobe Webshop and Logo Design

We need a complete design for our new Webshop
We sell pet accessories for dogs, cats, guinea pigs and some other animals
The provided logo ist a first draft for our logo and not final. you can be creative.
Maybe you can bring in some "Happyness" :o)
The Website will be a PageForge/Tradecraft System with a "ShopCanvas" Theme. We can provide a test environment, but it must be transferable to the final website.
In the First step, we need a finalized logo, then the WebDesign.

We need the following items.

* Company Icon
* Favicon 512*512 (from company icon)
* Shipping Label Icon (300px*100px, transparent background)
* Label Icon (600px*150px, transparent background)
* WebShop Design/Child-Theme
* Businesscard

Target Market(s)

German retail for pet accessories

Industry/Entity Type

Pet

Logo Text

SunnyPawGlobe

Coding

Coded - Design and coding required

Number of Pages Required

3 page

Colors

Designer to choose colors to be used in the design.

Requirements
Must have
• Cat, Dog, and Guineapig must be present
• The design must communicate happy pets.

```html
<!DOCTYPE html>
<html lang="en">
<head>
<meta charset="utf-8">
<title>SunnyPawGlobe – Pet Accessories</title>
<link href="https://fonts.googleapis.com/css2?family=Kaushan+Script&family=Montserrat:wght@400;600;700;800&family=Open+Sans:wght@400;600&display=swap" rel="stylesheet">
<style>
:root{
  --green:#7cb71f;
  --green-dark:#5f9514;
  --blue:#215c9d;
  --blue-deep:#1b4f88;
  --ink:#2d2d2d;
  --text:#555b61;
  --muted:#8a9097;
  --light:#eef1f4;
  --line:#dfe3e7;
  --white:#ffffff;
  --footer:#2a2b2d;
}
*{box-sizing:border-box;margin:0;padding:0}
html,body{width:1200px;height:3756px;overflow:hidden}
body{font-family:"Open Sans",Arial,sans-serif;color:var(--text);background:var(--white);position:relative}
.section{position:absolute;left:0;width:1200px}
.title-script{font-family:"Kaushan Script",cursive;text-align:center;color:var(--green);font-size:34px}
.title-script span{color:var(--blue);font-size:40px}
.btn{display:inline-block;font-family:"Montserrat",Arial,sans-serif;font-weight:600;font-size:14px;border-radius:22px;padding:11px 26px;text-decoration:none}
.btn-green{background:var(--green);color:var(--white)}
.btn-blue{background:var(--blue);color:var(--white)}
.btn-outline{border:2px solid var(--white);color:var(--white)}
.round-arrow{position:absolute;width:40px;height:40px;border-radius:50%;background:var(--green);display:flex;align-items:center;justify-content:center}

/* header */
.header{top:0;height:112px;background:var(--white);box-shadow:0 2px 8px rgba(0,0,0,.06);z-index:2}
.brand{position:absolute;left:60px;top:30px;display:flex;align-items:center;gap:12px}
.brand-dot{width:48px;height:48px;border-radius:50%;background:var(--blue)}
.brand-name{font-family:"Montserrat",Arial,sans-serif;font-weight:800;font-size:24px;color:var(--green)}
.nav{position:absolute;left:352px;top:62px;display:flex;gap:6px;font-family:"Montserrat",Arial,sans-serif;font-size:14px;font-weight:600}
.nav a{color:var(--ink);text-decoration:none;padding:8px 16px}
.nav a.active{color:var(--green);border:1px solid var(--line);border-radius:3px}
.call{position:absolute;left:720px;top:22px;font-family:"Montserrat",Arial,sans-serif;font-size:14px;color:var(--ink);font-weight:700;display:flex;align-items:center;gap:8px}
.call em{font-style:normal;color:var(--green)}
.search{position:absolute;left:880px;top:62px;width:150px;height:34px;border-bottom:1px solid var(--line);font-size:13px;color:var(--muted);padding:8px 4px}
.cart{position:absolute;left:1040px;top:22px;background:var(--blue);color:var(--white);font-family:"Montserrat",Arial,sans-serif;font-size:13px;font-weight:600;padding:9px 18px;border-radius:18px}

/* hero */
.hero{top:112px;height:500px;background:linear-gradient(100deg,#3f5a2c 0%,#6b7a3a 35%,#a69a7a 60%,#5f5a4a 100%)}
.hero-copy{position:absolute;left:72px;top:160px;width:420px;color:var(--white)}
.hero-kicker{font-family:"Kaushan Script",cursive;font-size:22px}
.hero-copy h1{font-family:"Montserrat",Arial,sans-serif;font-weight:800;font-size:44px;margin:6px 0 18px}
.hero-copy p{font-size:15px;line-height:1.6;margin-bottom:30px}
.hero-dots{position:absolute;left:100px;bottom:30px;display:flex;gap:8px}
.hero-dots i{width:26px;height:4px;background:rgba(255,255,255,.5)}
.hero-dots i:first-child{background:var(--white)}

/* categories */
.categories{top:612px;height:468px;background:var(--light)}
.categories .title-script{padding-top:66px}
.cat{position:absolute;top:170px;width:240px;text-align:center}
.cat-photo{width:184px;height:184px;border-radius:50%;margin:0 auto 24px;border:6px solid var(--white);box-shadow:0 4px 12px rgba(0,0,0,.1)}
.cat-name{font-family:"Montserrat",Arial,sans-serif;font-weight:600;font-size:17px;color:var(--ink)}
.cat-name.current{color:var(--blue);text-decoration:underline}

/* welcome */
.welcome{top:1080px;height:440px;background:var(--blue)}
.welcome-photo{position:absolute;left:88px;top:80px;width:476px;height:300px;background:linear-gradient(135deg,#d9c2a3,#9c7b55 55%,#4c4036)}
.welcome-copy{position:absolute;left:620px;top:100px;width:470px;color:var(--white);text-align:center}
.welcome-copy h2{font-family:"Montserrat",Arial,sans-serif;font-size:26px;font-weight:700;margin-bottom:24px}
.welcome-copy p{font-size:15px;line-height:1.7;margin-bottom:28px;padding:0 30px}
.welcome-cat{position:absolute;left:1076px;top:290px;width:124px;height:190px;background:linear-gradient(180deg,#e9a25b,#c97c3a);border-radius:60px 0 0 0}

/* products */
.products{top:1520px;height:720px;background:var(--white)}
.products .title-script{padding-top:70px}
.card{position:absolute;top:196px;width:228px;height:410px;background:var(--white);border:1px solid var(--line);text-align:center}
.card.featured{box-shadow:0 8px 24px rgba(0,0,0,.15)}
.card-photo{height:210px;margin:12px}
.card-text{font-size:15px;color:var(--text);padding:8px 24px 10px;line-height:1.4}
.card-price{font-family:"Montserrat",Arial,sans-serif;font-weight:700;font-size:22px;color:var(--green);margin-bottom:14px}
.card .btn{font-size:13px;padding:8px 20px;border:1px solid var(--line);color:var(--ink)}
.card.featured .btn{background:var(--green);color:var(--white);border-color:var(--green)}
.view-all{position:absolute;top:612px;left:0;width:1200px;text-align:center}

/* testimonial */
.pets-peek{position:absolute;top:2212px;left:460px;width:300px;height:182px;background:linear-gradient(180deg,#d79a55,#b57a40);border-radius:90px 90px 0 0;z-index:1}
.testimonial{top:2300px;height:470px;background:var(--green);color:var(--white);text-align:center}
.quote-mark{font-family:Georgia,serif;font-size:64px;padding-top:70px;line-height:1}
.testimonial blockquote{font-size:28px;line-height:1.5;width:800px;margin:16px auto 26px}
.testimonial cite{font-family:"Montserrat",Arial,sans-serif;font-style:normal;font-weight:700;font-size:17px}
.t-dots{display:flex;justify-content:center;gap:6px;margin-top:30px}
.t-dots i{width:30px;height:4px;background:rgba(255,255,255,.5)}
.t-dots i:nth-child(2){background:var(--blue)}
.testimonial .round-arrow{background:var(--white)}
.testimonial .round-arrow.right{background:var(--blue)}

/* blog */
.blog{top:2770px;height:582px;background:var(--white)}
.blog .title-script{padding-top:60px}
.post{position:absolute;top:172px;width:500px}
.post-date{position:absolute;left:0;top:0;width:70px;text-align:center;font-family:"Montserrat",Arial,sans-serif}
.post-date b{display:block;font-size:38px;color:var(--blue)}
.post-date small{display:block;font-size:12px;color:var(--muted);border-bottom:1px solid var(--line);padding-bottom:22px;margin-bottom:22px}
.post-date b.green{color:var(--green)}
.post-photo{position:absolute;left:96px;top:0;width:400px;height:200px}
.post-title{position:absolute;left:96px;top:218px;width:380px;font-family:"Montserrat",Arial,sans-serif;font-weight:600;font-size:17px;line-height:1.45;color:var(--blue-deep);text-decoration:underline}
.blog-all{position:absolute;top:480px;width:1200px;text-align:center}

/* features */
.features{top:3352px;height:136px;display:flex}
.feature{width:400px;display:flex;flex-direction:column;align-items:center;justify-content:center;gap:12px;color:var(--white);font-family:"Montserrat",Arial,sans-serif;font-weight:700;font-size:19px}
.feature.dark{background:#333436}
.feature.green{background:var(--green)}
.feature.blue{background:var(--blue)}

/* footer */
.footer{top:3488px;height:268px;background:var(--footer);color:#c8ccd0}
.footer .brand{left:60px;top:48px}
.footer .brand-name{color:var(--white)}
.footer-nav{position:absolute;left:60px;top:128px;display:flex;gap:28px;font-family:"Montserrat",Arial,sans-serif;font-size:14px}
.footer-nav a{color:#c8ccd0;text-decoration:none}
.footer-nav a.active{color:var(--green);text-decoration:underline}
.copyright{position:absolute;left:60px;top:172px;font-size:13px;color:var(--muted)}
.subscribe{position:absolute;left:680px;top:48px;display:flex}
.subscribe .field{width:300px;height:44px;background:#3a3b3e;border-radius:22px 0 0 22px;padding:13px 20px;font-size:13px;color:var(--muted)}
.subscribe .go{height:44px;background:var(--green);color:var(--white);border-radius:0 22px 22px 0;padding:13px 28px;font-family:"Montserrat",Arial,sans-serif;font-weight:600;font-size:14px}
.sub-note{position:absolute;left:700px;top:112px;font-size:13px}
.social{position:absolute;left:880px;top:152px;display:flex;gap:10px}
.social i{width:34px;height:34px;border-radius:50%;border:1px solid #6a6d72}
.social i.on{background:var(--green);border-color:var(--green)}
</style>
</head>
<body>

<header class="section header">
  <div class="brand"><div class="brand-dot"></div><div class="brand-name">SunnyPawGlobe</div></div>
  <div class="call">
    <svg width="16" height="16" viewBox="0 0 24 24"><path fill="#7cb71f" d="M6.6 10.8a15 15 0 0 0 6.6 6.6l2.2-2.2c.3-.3.7-.4 1-.2 1.1.4 2.3.6 3.6.6.6 0 1 .4 1 1V20c0 .6-.4 1-1 1A17 17 0 0 1 3 4c0-.6.4-1 1-1h3.5c.6 0 1 .4 1 1 0 1.3.2 2.5.6 3.6.1.3 0 .7-.2 1z"/></svg>
    <em>Call Us:</em> 123 - 456 - 7890
  </div>
  <nav class="nav">
    <a class="active">Home</a><a>Shop</a><a>Blog</a><a>Shopping Cart</a><a>Contact Us</a>
  </nav>
  <div class="search">Search</div>
  <div class="cart">Cart $0.00</div>
</header>

<section class="section hero" role="img" aria-label="Photo of a groomed small dog with a red bow sitting on a green lawn">
  <div class="hero-copy">
    <div class="hero-kicker">SunnyPawGlobe</div>
    <h1>We Style Your Pet</h1>
    <p>There are many variations of passages of Lorem Ipsum available, but the majority have suffered...</p>
    <a class="btn btn-outline">Shop Now!</a>
  </div>
  <div class="round-arrow" style="left:18px;top:230px;background:var(--white)">
    <svg width="14" height="14" viewBox="0 0 24 24"><path d="M15 5l-7 7 7 7" stroke="#2d2d2d" stroke-width="3" fill="none"/></svg>
  </div>
  <div class="round-arrow" style="left:1142px;top:200px;background:var(--white)">
    <svg width="14" height="14" viewBox="0 0 24 24"><path d="M9 5l7 7-7 7" stroke="#2d2d2d" stroke-width="3" fill="none"/></svg>
  </div>
  <div class="hero-dots"><i></i><i></i><i></i></div>
</section>

<section class="section categories">
  <h2 class="title-script">Shop By <span>Categories</span></h2>
  <div class="cat" style="left:100px"><div class="cat-photo" role="img" aria-label="Photo of a puppy on grass" style="background:linear-gradient(160deg,#9dbf63,#c9a26f)"></div><div class="cat-name">Dogs Accessories</div></div>
  <div class="cat" style="left:360px"><div class="cat-photo" role="img" aria-label="Photo of a grey cat" style="background:linear-gradient(160deg,#6f9ccf,#4d6a8e)"></div><div class="cat-name current">Cat Accessories</div></div>
  <div class="cat" style="left:620px"><div class="cat-photo" role="img" aria-label="Photo of a guinea pig" style="background:linear-gradient(160deg,#b0c98a,#8a6a45)"></div><div class="cat-name">Guinea Pigs Accessories</div></div>
  <div class="cat" style="left:880px"><div class="cat-photo" role="img" aria-label="Photo of a squirrel on a branch" style="background:linear-gradient(160deg,#7d9a4a,#a4552b)"></div><div class="cat-name">Other Animals</div></div>
</section>

<section class="section welcome">
  <div class="welcome-photo" role="img" aria-label="Photo of a smiling woman hugging her dog"></div>
  <div class="welcome-copy">
    <h2>Welcome to SunnyPawGlobe</h2>
    <p>Contrary to popular belief, Lorem Ipsum is not simply random text. It has roots in a piece of classical Latin literature from 45 BC, making it over 2000 years old. Harold Brenwick, a Latin professor at Ashford Vale...</p>
    <a class="btn btn-green">Discover More</a>
  </div>
  <div class="welcome-cat" role="img" aria-label="Illustration of a ginger cat peeking in from the edge"></div>
</section>

<section class="section products">
  <h2 class="title-script">Shop Our <span>Products</span></h2>
  <div class="round-arrow" style="left:64px;top:400px">
    <svg width="14" height="14" viewBox="0 0 24 24"><path d="M15 5l-7 7 7 7" stroke="#fff" stroke-width="3" fill="none"/></svg>
  </div>
  <div class="card" style="left:100px"><div class="card-photo" role="img" aria-label="Photo of a brown leather dog collar" style="background:linear-gradient(135deg,#f3ece4,#c9a27c)"></div><p class="card-text">It is a long established fact that</p><div class="card-price">€14.99</div><a class="btn">Shop Now!</a></div>
  <div class="card featured" style="left:352px"><div class="card-photo" role="img" aria-label="Photo of a pet carrier bag" style="background:linear-gradient(135deg,#eef3f8,#8fb0d4)"></div><p class="card-text">It is a long established fact that</p><div class="card-price">€89.99</div><a class="btn">Shop Now!</a></div>
  <div class="card" style="left:608px"><div class="card-photo" role="img" aria-label="Photo of a small dog wearing a red plaid coat" style="background:linear-gradient(135deg,#f3eded,#b6434a)"></div><p class="card-text">It is a long established fact that</p><div class="card-price">€12.99</div><a class="btn">Shop Now!</a></div>
  <div class="card" style="left:862px"><div class="card-photo" role="img" aria-label="Photo of a brown covered cat bed" style="background:linear-gradient(135deg,#f1ece6,#7a5a42)"></div><p class="card-text">It is a long established fact that</p><div class="card-price">€20.99</div><a class="btn">Shop Now!</a></div>
  <div class="round-arrow" style="left:1106px;top:400px">
    <svg width="14" height="14" viewBox="0 0 24 24"><path d="M9 5l7 7-7 7" stroke="#fff" stroke-width="3" fill="none"/></svg>
  </div>
  <div class="view-all"><a class="btn btn-blue">View All Products</a></div>
</section>

<div class="pets-peek" role="img" aria-label="Photo of a dog and a kitten peeking over the edge"></div>

<section class="section testimonial">
  <div class="quote-mark">&ldquo;</div>
  <blockquote>Contrary to popular belief, Lorem Ipsum is not simply random text. It has roots in a piece of classical Latin literature from 45 BC, making it over years old...</blockquote>
  <cite>Standard Chunk</cite>
  <div class="t-dots"><i></i><i></i><i></i></div>
  <div class="round-arrow" style="left:90px;top:200px">
    <svg width="14" height="14" viewBox="0 0 24 24"><path d="M15 5l-7 7 7 7" stroke="#7cb71f" stroke-width="3" fill="none"/></svg>
  </div>
  <div class="round-arrow right" style="left:1010px;top:170px">
    <svg width="14" height="14" viewBox="0 0 24 24"><path d="M9 5l7 7-7 7" stroke="#fff" stroke-width="3" fill="none"/></svg>
  </div>
</section>

<section class="section blog">
  <h2 class="title-script">Latest <span>Blog</span></h2>
  <article class="post" style="left:110px">
    <div class="post-date"><b>15</b><small>March 2017</small><b class="green">30</b><small style="border:0">Comments</small></div>
    <div class="post-photo" role="img" aria-label="Photo of a guinea pig" style="background:linear-gradient(135deg,#c7b8a6,#6d5d4e)"></div>
    <div class="post-title">Distracted by the readable content of a page more-or-less normal...</div>
  </article>
  <article class="post" style="left:630px">
    <div class="post-date"><b>25</b><small>March 2017</small><b class="green">35</b><small style="border:0">Comments</small></div>
    <div class="post-photo" role="img" aria-label="Photo of a white dog lying on a sofa" style="background:linear-gradient(135deg,#e9dfd0,#b59470)"></div>
    <div class="post-title">Distracted by the readable content of a page more-or-less normal...</div>
  </article>
  <div class="blog-all"><a class="btn btn-green">View All Blog</a></div>
</section>

<section class="section features">
  <div class="feature dark">
    <svg width="36" height="36" viewBox="0 0 24 24" fill="none" stroke="#fff" stroke-width="2"><path d="M4 14v-2a8 8 0 0 1 16 0v2"/><rect x="3" y="13" width="4" height="6" rx="1"/><rect x="17" y="13" width="4" height="6" rx="1"/></svg>
    24/7 Support
  </div>
  <div class="feature green">
    <svg width="36" height="36" viewBox="0 0 24 24" fill="none" stroke="#fff" stroke-width="2"><path d="M20 12a8 8 0 1 1-2.3-5.7"/><path d="M20 4v5h-5"/></svg>
    <span style="text-decoration:underline">30-Day Returns</span>
  </div>
  <div class="feature blue">
    <svg width="40" height="36" viewBox="0 0 26 24" fill="none" stroke="#fff" stroke-width="2"><rect x="2" y="6" width="13" height="10"/><path d="M15 9h5l4 4v3h-9z"/><circle cx="7" cy="18" r="2"/><circle cx="19" cy="18" r="2"/></svg>
    Free Shipping
  </div>
</section>

<footer class="section footer">
  <div class="brand"><div class="brand-dot"></div><div class="brand-name">SunnyPawGlobe</div></div>
  <nav class="footer-nav"><a class="active">Home</a><a>Shop</a><a>Blog</a><a>Shopping Cart</a><a>Contact Us</a></nav>
  <div class="copyright">© 2017 SunnyPawGlobe. All rights reserved.</div>
  <div class="subscribe"><div class="field">Enter your Email...</div><div class="go">Subscribe</div></div>
  <div class="sub-note">Subscribe to our mailing list to get the latest updates</div>
  <div class="social"><i></i><i></i><i></i><i></i><i></i><i class="on"></i></div>
</footer>

</body>
</html>
```